Need LMS Harborkit Site with full online course and student support

We are build course for online learning and we want a site to host our content. We would like a HK site using one of the LMS plugins (like brenqus, tovadesk (https://tovadesk.example/, etc.).

When finished, the deliverable should simply required us to:
1. put it in place
a) should have Quenthall images, logo, and themed with Quenthall colors (blue and orange)
2. change tag line/moto
3. configured it with our db
4. configure zelmora account to receive payment
5. delete sample data/courses
6. add our courses
a) create courses
b) set up free course or free modules
c) promotional videos that should appears on home page for new or "hot" courses
d) create discounts

Please see the promo video for tovadesk.

What would it take to have a site like this? Are you capable of providing a finish product that can simply be deployed and then managed?

Thanks for your time.

Target Market(s)

Online learning

Industry/Entity Type

Computer Training

Number of Pages Required

5+ page

Font styles to use
Serif

Colors
3176b5
f78f20
faa54b
f37122
f68d4d
0255a3
0692cd

Requirements
Must have
• 1. put it in place
• a) should have Quenthall images, logo, and themed with Quenthall colors (blue and orange)
• 2. change tag line/moto
• 3. configured it with our db
• 4. configure zelmora account to receive payment
• 5. delete sample data/course
• 6. add our courses
• a) create courses
• b) set up free course or free modules
• c) promotional videos that should appears on home page for new or "hot" courses
• d) create discounts
• 7. students have their own account
• 8. discussion area
• 9. testing
• Please see sites like https://mavilearn.example, https://pondrix.example, and https://glenwick.example.

```html
<!DOCTYPE html>
<html lang="en">
<head>
<meta charset="utf-8">
<title>Quenthall – Online Courses &amp; Student Support</title>
<link href="https://fonts.googleapis.com/css2?family=Open+Sans:wght@300;400;600;700;800&display=swap" rel="stylesheet">
<style>
  :root {
    --blue: #3176b5;
    --blue-deep: #0255a3;
    --blue-sky: #0692cd;
    --orange: #f37122;
    --orange-soft: #faa54b;
    --orange-mid: #f78f20;
    --ink: #333333;
    --muted: #888888;
    --line: #dcdcdc;
    --band: #f0f0f0;
    --footer: #2f6fb5;
  }
  * { box-sizing: border-box; margin: 0; padding: 0; }
  html, body { width: 1200px; height: 3435px; overflow: hidden; }
  body { font-family: "Open Sans", Arial, sans-serif; color: var(--ink); background: #fff; position: relative; }
  a { color: inherit; text-decoration: none; }

  /* Header */
  .site-header { position: absolute; left: 0; top: 0; width: 1200px; height: 119px; background: #fff; }
  .brand { position: absolute; left: 128px; top: 32px; display: flex; align-items: center; gap: 10px; }
  .brand-dot { width: 40px; height: 40px; border-radius: 50%; background: var(--blue-deep); }
  .brand-name { font-size: 28px; font-weight: 700; color: var(--blue-deep); }
  .search { position: absolute; left: 714px; top: 21px; width: 241px; height: 37px; border: 1px solid #cfcfcf; display: flex; align-items: center; padding-left: 14px; gap: 10px; font-size: 12px; color: #666; }
  .btn-signin { position: absolute; left: 975px; top: 21px; width: 92px; height: 37px; background: var(--orange); color: #fff; font-size: 13px; font-weight: 600; display: flex; align-items: center; justify-content: center; }
  .main-nav { position: absolute; top: 78px; left: 630px; display: flex; gap: 0; font-size: 13px; }
  .main-nav a { display: block; height: 28px; line-height: 28px; padding: 0 10px; }
  .main-nav a.current { background: var(--blue); color: #fff; }
  .main-nav .n1 { margin-right: 16px; } .main-nav .n2 { margin-right: 14px; } .main-nav .n3 { margin-right: 14px; } .main-nav .n4 { margin-right: 14px; }

  /* Hero */
  .hero { position: absolute; left: 0; top: 119px; width: 1200px; height: 481px; }
  .hero-photo { position: absolute; inset: 0; background: linear-gradient(100deg, #2f7cc9 0%, #3d8ad3 45%, #4f95d6 70%, #2a6fb6 100%); }
  .hero-title { position: absolute; left: 126px; top: 120px; color: #fff; font-size: 44px; line-height: 52px; }
  .hero-title strong { font-weight: 800; display: block; }
  .hero-title span { font-weight: 300; display: block; }
  .hero-dots { position: absolute; left: 548px; top: 398px; display: flex; gap: 14px; align-items: center; }
  .hero-dots i { width: 8px; height: 8px; border-radius: 50%; background: #fff; display: block; }
  .hero-dots i.active { width: 12px; height: 12px; background: transparent; border: 2px solid #fff; }

  /* Welcome */
  .welcome { position: absolute; left: 128px; top: 561px; width: 939px; height: 298px; background: #fff; border: 3px solid var(--blue); }
  .welcome-text { position: absolute; left: 57px; top: 78px; width: 470px; }
  .welcome h2 { font-size: 17px; font-weight: 700; color: var(--blue-deep); margin-bottom: 18px; }
  .welcome p { font-size: 13px; line-height: 24px; color: #555; }
  .btn-read { position: absolute; left: 57px; top: 214px; width: 105px; height: 35px; background: var(--orange); color: #fff; font-size: 11px; font-weight: 700; display: flex; align-items: center; justify-content: center; }
  .welcome-divider { position: absolute; left: 563px; top: 78px; width: 1px; height: 140px; background: var(--line); }
  .welcome-mark { position: absolute; left: 620px; top: 110px; width: 260px; display: flex; align-items: center; justify-content: center; gap: 14px; }
  .welcome-mark .dot { width: 54px; height: 54px; border-radius: 50%; background: var(--blue-deep); }
  .welcome-mark .word { font-size: 34px; font-weight: 700; color: var(--blue-deep); }

  /* Section titles */
  .section-title { position: absolute; left: 0; width: 1200px; text-align: center; font-size: 24px; font-weight: 700; color: var(--blue-deep); letter-spacing: .3px; }
  .section-title .arrow { display: inline-block; vertical-align: middle; margin: 0 32px; }

  /* Course cards */
  .course-grid { position: absolute; left: 128px; display: grid; grid-template-columns: repeat(4, 224px); column-gap: 14px; row-gap: 16px; }
  .course-card { height: 314px; border: 1px solid var(--line); background: #fff; position: relative; }
  .course-media { height: 140px; position: relative; }
  .course-media .play { position: absolute; left: 50%; top: 50%; width: 46px; height: 46px; margin: -23px 0 0 -23px; }
  .course-body { padding: 28px 22px 0; }
  .course-cat { font-size: 10px; color: var(--muted); margin-bottom: 14px; }
  .course-name { font-size: 13px; line-height: 21px; color: #333; height: 42px; }
  .course-count { display: inline-block; margin-top: 18px; border: 1px solid var(--blue); color: var(--blue); font-size: 10px; padding: 5px 10px; }
  .m1 { background: linear-gradient(135deg, #5a87b8, #c7d6e6); }
  .m2 { background: linear-gradient(135deg, #1c2f4c, #4e6f9a); }
  .m3 { background: linear-gradient(135deg, #8a8f96, #c9cdd2); }
  .m4 { background: linear-gradient(135deg, #6b7480, #d8dde2); }
  .m5 { background: linear-gradient(135deg, #e9ecef, #b9c2cc); }
  .m6 { background: linear-gradient(135deg, #5a4a3c, #a58e74); }
  .m7 { background: linear-gradient(135deg, #d9d9d9, #9a9ea3); }
  .m8 { background: linear-gradient(135deg, #c7a57b, #e5d6c3); }
  .m9 { background: linear-gradient(135deg, #b7cbe0, #edf2f7); }
  .m10 { background: linear-gradient(135deg, #3b2f2a, #9a8070); }
  .m11 { background: linear-gradient(135deg, #1f4fa8, #e39a4a); }
  .m12 { background: linear-gradient(135deg, #7f8790, #e0e3e6); }

  /* Why choose us */
  .why-grid { position: absolute; left: 128px; top: 2281px; display: flex; gap: 36px; }
  .why-card { width: 289px; height: 252px; background: #fff; box-shadow: 0 2px 12px rgba(0,0,0,.16); text-align: center; padding-top: 28px; }
  .why-card svg { display: block; margin: 0 auto 22px; }
  .why-card h3 { font-size: 17px; font-weight: 400; color: #222; margin-bottom: 12px; }
  .why-card p { font-size: 11px; line-height: 18px; color: #555; width: 190px; margin: 0 auto; }

  /* Testimonials */
  .testimonials { position: absolute; left: 0; top: 2627px; width: 1200px; height: 396px; background: var(--band); }
  .testimonials h2 { position: absolute; top: 78px; width: 1200px; text-align: center; font-size: 24px; font-weight: 700; color: var(--blue-deep); }
  .quote { position: absolute; left: 280px; top: 150px; width: 640px; text-align: center; font-size: 14px; line-height: 26px; color: #666; }
  .quote-author { position: absolute; top: 302px; width: 1200px; text-align: center; font-size: 11px; color: var(--blue); }
  .quote-place { position: absolute; top: 322px; width: 1200px; text-align: center; font-size: 9px; color: #555; }
  .t-arrow { position: absolute; top: 168px; }

  /* Footer */
  .site-footer { position: absolute; left: 0; top: 3023px; width: 1200px; height: 412px; background: var(--footer); color: #fff; }
  .footer-brand { position: absolute; left: 128px; top: 66px; display: flex; align-items: center; gap: 10px; }
  .footer-brand .dot { width: 34px; height: 34px; border-radius: 50%; background: #fff; }
  .footer-brand .word { font-size: 26px; font-weight: 700; color: #fff; }
  .footer-col { position: absolute; top: 66px; }
  .footer-col h4 { font-size: 11px; font-weight: 700; letter-spacing: .5px; margin-bottom: 26px; }
  .footer-col li { list-style: none; font-size: 10px; line-height: 20px; opacity: .9; }
  .footer-col .social li { display: flex; align-items: center; gap: 8px; line-height: 24px; }
  .footer-col .social i { width: 8px; height: 8px; background: #fff; border-radius: 50%; display: block; }
  .news-input { position: absolute; left: 824px; top: 110px; width: 243px; height: 48px; background: #fff; color: #888; font-size: 11px; padding-left: 18px; display: flex; align-items: center; }
  .btn-signup { position: absolute; left: 953px; top: 174px; width: 114px; height: 41px; background: var(--orange-soft); color: #fff; font-size: 15px; font-weight: 700; display: flex; align-items: center; justify-content: center; }
  .footer-rule { position: absolute; left: 128px; top: 311px; width: 939px; height: 1px; background: rgba(255,255,255,.3); }
  .copyright { position: absolute; top: 350px; width: 1200px; text-align: center; font-size: 10px; opacity: .85; }
</style>
</head>
<body>

<header class="site-header">
  <a class="brand" href="#"><span class="brand-dot"></span><span class="brand-name">Quenthall</span></a>
  <div class="search">
    <svg width="12" height="12" viewBox="0 0 12 12"><circle cx="5" cy="5" r="3.6" fill="none" stroke="#555" stroke-width="1.4"/><line x1="7.7" y1="7.7" x2="11" y2="11" stroke="#555" stroke-width="1.4"/></svg>
    Search
  </div>
  <a class="btn-signin" href="#">SIGN IN</a>
  <nav class="main-nav">
    <a class="current n1" href="#">Home</a>
    <a class="n2" href="#">About us</a>
    <a class="n3" href="#">Services</a>
    <a class="n4" href="#">Blog</a>
    <a href="#">Contact us</a>
  </nav>
</header>

<section class="hero">
  <div class="hero-photo" role="img" aria-label="Blue-toned photo of a student working at a laptop in a bright office"></div>
  <h1 class="hero-title"><strong>Best online courses &amp;</strong><span>Student Support</span></h1>
  <div class="hero-dots"><i></i><i class="active"></i><i></i><i></i><i></i></div>
</section>

<section class="welcome">
  <div class="welcome-text">
    <h2>WELCOME TO OUR SITE</h2>
    <p>It is a long established fact that a reader will be distracted by the readable content of a page when looking at its layout. The point of using Lorem Ipsum is that it has a more-or-less.</p>
  </div>
  <a class="btn-read" href="#">READ MORE</a>
  <div class="welcome-divider"></div>
  <div class="welcome-mark"><span class="dot"></span><span class="word">Quenthall</span></div>
</section>

<h2 class="section-title" style="top:918px">LATEST COURSES</h2>

<div class="course-grid" style="top:1003px">
  <article class="course-card"><div class="course-media m1" role="img" aria-label="Course video still: laptop on a desk"><svg class="play" viewBox="0 0 46 46"><circle cx="23" cy="23" r="21" fill="var(--orange)" opacity=".85"/><path d="M18 14 L32 23 L18 32Z" fill="#fff"/></svg></div><div class="course-body"><div class="course-cat">Lorem ipsum</div><div class="course-name">It is a long established fact that</div><span class="course-count">10 Courses</span></div></article>
  <article class="course-card"><div class="course-media m2" role="img" aria-label="Course video still: code on a dark screen"><svg class="play" viewBox="0 0 46 46"><circle cx="23" cy="23" r="21" fill="var(--orange)" opacity=".85"/><path d="M18 14 L32 23 L18 32Z" fill="#fff"/></svg></div><div class="course-body"><div class="course-cat">Lorem ipsum</div><div class="course-name">Lorem Ipsum is simply dummy text of the</div><span class="course-count">10 Courses</span></div></article>
  <article class="course-card"><div class="course-media m3" role="img" aria-label="Course video still: open-plan study room"><svg class="play" viewBox="0 0 46 46"><circle cx="23" cy="23" r="21" fill="var(--orange)" opacity=".85"/><path d="M18 14 L32 23 L18 32Z" fill="#fff"/></svg></div><div class="course-body"><div class="course-cat">Lorem ipsum</div><div class="course-name">There are many variations of passages of Lorem</div><span class="course-count">10 Courses</span></div></article>
  <article class="course-card"><div class="course-media m4" role="img" aria-label="Course video still: student in a library with a laptop"><svg class="play" viewBox="0 0 46 46"><circle cx="23" cy="23" r="21" fill="var(--orange)" opacity=".85"/><path d="M18 14 L32 23 L18 32Z" fill="#fff"/></svg></div><div class="course-body"><div class="course-cat">Lorem ipsum</div><div class="course-name">Lorem Ipsum generators on the Interne</div><span class="course-count">10 Courses</span></div></article>
  <article class="course-card"><div class="course-media m5" role="img" aria-label="Course video still: writing on a glass board"><svg class="play" viewBox="0 0 46 46"><circle cx="23" cy="23" r="21" fill="var(--orange)" opacity=".85"/><path d="M18 14 L32 23 L18 32Z" fill="#fff"/></svg></div><div class="course-body"><div class="course-cat">Lorem ipsum</div><div class="course-name">Word in classical literature discovered the</div><span class="course-count">10 Courses</span></div></article>
  <article class="course-card"><div class="course-media m6" role="img" aria-label="Course video still: group working around a table"><svg class="play" viewBox="0 0 46 46"><circle cx="23" cy="23" r="21" fill="var(--orange)" opacity=".85"/><path d="M18 14 L32 23 L18 32Z" fill="#fff"/></svg></div><div class="course-body"><div class="course-cat">Lorem ipsum</div><div class="course-name">All the Lorem Ipsum gener ators on lorem</div><span class="course-count">10 Courses</span></div></article>
  <article class="course-card"><div class="course-media m7" role="img" aria-label="Course video still: hand sketching on paper"><svg class="play" viewBox="0 0 46 46"><circle cx="23" cy="23" r="21" fill="var(--orange)" opacity=".85"/><path d="M18 14 L32 23 L18 32Z" fill="#fff"/></svg></div><div class="course-body"><div class="course-cat">Lorem ipsum</div><div class="course-name">Various versions have evol ved over the years</div><span class="course-count">10 Courses</span></div></article>
  <article class="course-card"><div class="course-media m8" role="img" aria-label="Course video still: hands on a laptop keyboard"><svg class="play" viewBox="0 0 46 46"><circle cx="23" cy="23" r="21" fill="var(--orange)" opacity=".85"/><path d="M18 14 L32 23 L18 32Z" fill="#fff"/></svg></div><div class="course-body"><div class="course-cat">Lorem ipsum</div><div class="course-name">Model sentence structures to generate Lorem</div><span class="course-count">10 Courses</span></div></article>
</div>

<h2 class="section-title" style="top:1715px">
  <svg class="arrow" width="14" height="24" viewBox="0 0 14 24"><path d="M12 2 L3 12 L12 22" fill="none" stroke="#aaa" stroke-width="2"/></svg>POPULAR COURSES<svg class="arrow" width="14" height="24" viewBox="0 0 14 24"><path d="M2 2 L11 12 L2 22" fill="none" stroke="#aaa" stroke-width="2"/></svg>
</h2>

<div class="course-grid" style="top:1800px">
  <article class="course-card"><div class="course-media m9" role="img" aria-label="Course photo: laboratory glassware"></div><div class="course-body"><div class="course-cat">Lorem ipsum</div><div class="course-name">It is a long established fact that</div><span class="course-count">10 Courses</span></div></article>
  <article class="course-card"><div class="course-media m10" role="img" aria-label="Course photo: audio mixing desk"></div><div class="course-body"><div class="course-cat">Lorem ipsum</div><div class="course-name">Lorem Ipsum is simply dummy text of the</div><span class="course-count">10 Courses</span></div></article>
  <article class="course-card"><div class="course-media m11" role="img" aria-label="Course photo: science experiment with test tubes"></div><div class="course-body"><div class="course-cat">Lorem ipsum</div><div class="course-name">There are many variations of passages of Lorem</div><span class="course-count">10 Courses</span></div></article>
  <article class="course-card"><div class="course-media m12" role="img" aria-label="Course photo: hand using a laptop"></div><div class="course-body"><div class="course-cat">Lorem ipsum</div><div class="course-name">Lorem Ipsum generators on the Interne</div><span class="course-count">10 Courses</span></div></article>
</div>

<h2 class="section-title" style="top:2192px">WHY CHOOSE US</h2>

<div class="why-grid">
  <div class="why-card">
    <svg width="56" height="62" viewBox="0 0 56 62"><rect x="9" y="4" width="38" height="46" rx="3" fill="none" stroke="var(--orange)" stroke-width="3"/><line x1="17" y1="16" x2="39" y2="16" stroke="var(--orange)" stroke-width="3"/><line x1="17" y1="24" x2="39" y2="24" stroke="var(--orange)" stroke-width="3"/><circle cx="28" cy="40" r="6" fill="var(--orange)"/><path d="M24 45 L22 58 L28 54 L34 58 L32 45" fill="var(--orange)"/></svg>
    <h3>Valuable Certificate</h3>
    <p>It is a long established fact that a reader will be distracted by the readable content o</p>
  </div>
  <div class="why-card">
    <svg width="56" height="62" viewBox="0 0 56 62"><circle cx="28" cy="22" r="17" fill="var(--orange)"/><circle cx="28" cy="22" r="9" fill="none" stroke="#fff" stroke-width="2.5"/><path d="M21 37 L21 60 L28 54 L35 60 L35 37Z" fill="var(--orange)"/></svg>
    <h3>Professional Certificate</h3>
    <p>It is a long established fact that a reader will be distracted by the readable content o</p>
  </div>
  <div class="why-card">
    <svg width="70" height="62" viewBox="0 0 70 62"><rect x="12" y="12" width="46" height="32" fill="none" stroke="var(--orange)" stroke-width="3"/><path d="M4 48 H66 L62 54 H8Z" fill="var(--orange)"/><path d="M35 20 L48 26 L35 32 L22 26Z" fill="var(--orange)"/><path d="M28 29 V35 H42 V29" fill="var(--orange)"/></svg>
    <h3>Online Programs</h3>
    <p>It is a long established fact that a reader will be distracted by the readable content o</p>
  </div>
</div>

<section class="testimonials">
  <h2>TESTIMONIALS</h2>
  <svg class="t-arrow" style="left:128px" width="22" height="52" viewBox="0 0 22 52"><path d="M19 2 L3 26 L19 50" fill="none" stroke="#d6d6d6" stroke-width="3"/></svg>
  <p class="quote">There are many variations of passages of Lorem Ipsum available, but the majority have suffered alteration in some form, by injected humour, or randomised words which don't look even slightly believable. If you are going to use a passage of Lorem Ipsum, you need to be sure there isn't anything embarrassing</p>
  <div class="quote-author">Marcus Delford</div>
  <div class="quote-place">Australia</div>
  <svg class="t-arrow" style="left:1045px" width="22" height="52" viewBox="0 0 22 52"><path d="M3 2 L19 26 L3 50" fill="none" stroke="#d6d6d6" stroke-width="3"/></svg>
</section>

<footer class="site-footer">
  <div class="footer-brand"><span class="dot"></span><span class="word">Quenthall</span></div>
  <div class="footer-col" style="left:346px">
    <h4>MENU</h4>
    <ul><li>Home</li><li>About us</li><li>services</li><li>Blog</li><li>Contact us</li></ul>
  </div>
  <div class="footer-col" style="left:483px">
    <h4>LINKS</h4>
    <ul><li>Terms</li><li>Privacy</li><li>Help</li><li>Accessibility</li><li>Press</li><li>Contact</li><li>Directory</li><li>Affiliates</li></ul>
  </div>
  <div class="footer-col" style="left:627px">
    <h4>FOLLOW US ON</h4>
    <ul class="social"><li><i></i>Chirpnest</li><li><i></i>Flitline</li><li><i></i>Workloom</li><li><i></i>RSS Feed</li></ul>
  </div>
  <div class="footer-col" style="left:824px">
    <h4>NEWSLETTER SIGNUP</h4>
  </div>
  <div class="news-input">E-mail id</div>
  <a class="btn-signup" href="#">SIGNUP</a>
  <div class="footer-rule"></div>
  <div class="copyright">Copyrights © 2017 All Rights Reserved</div>
</footer>

</body>
</html>
```